Clear Road Rentals flyer

Need a A6 size horizontal layout flyer. See attached example for ideas as well as some images I have which you can use. we are a hire car company that provides vehicles to clients who have recently been involved in car accidents and who's cars are currently getting fixed and so they lose the use of their own vehicle. see our website to keep flyer in line with website and for any further information clearroadrentals.com.au

Target Market(s)

people involved in not at fault car accidents

Industry/Entity Type

It Company

Requirements
Must have
• *ask people to let us know where they got our flyer from when they call us
• *call to action for people to call our phone number 1800 452 817
Should not have
• any mentioning that the vehicle is free

```html
<!DOCTYPE html>
<html lang="en">
<head>
<meta charset="utf-8">
<title>Clear Road Rentals Flyer</title>
<link href="https://fonts.googleapis.com/css2?family=Roboto:wght@400;500;700&family=Roboto+Condensed:wght@300;400;700&display=swap" rel="stylesheet">
<style>
  :root {
    --stage: #9bbbe3;
    --brand-blue: #5f8bcf;
    --band-top: #6a95d6;
    --band-bottom: #4a73ba;
    --step-light: #75a0da;
    --step-dark: #3f6db5;
    --accent-yellow: #f2b942;
    --box-border: #2b4678;
    --box-fill: #4f7cc3;
    --ink: #2f2f2f;
    --link-blue: #2f62b5;
    --white: #ffffff;
  }
  * { box-sizing: border-box; margin: 0; padding: 0; }
  html, body { width: 1199px; height: 1200px; overflow: hidden; }
  body { background: var(--stage); font-family: "Roboto", sans-serif; position: relative; }

  .flyer { position: absolute; left: 50px; top: 210px; width: 1100px; height: 780px; background: var(--white); overflow: hidden; }

  .hero-photo { position: absolute; top: 0; height: 200px; }
  .hero-photo--car { left: 0; width: 520px; background: linear-gradient(135deg, #6f7f8c 0%, #b8c4cf 45%, #55626d 100%); }
  .hero-photo--drivers { left: 520px; width: 580px; background: linear-gradient(160deg, #7d9ccc 0%, #c9d4e4 50%, #5d7fb8 100%); }

  .brand-banner { position: absolute; left: 0; top: 120px; width: 1100px; height: 140px; }
  .owned-badge { position: absolute; left: 752px; top: 132px; width: 30px; height: 20px; border-radius: 4px; background: var(--white); }
  .brand-name { position: absolute; left: 0; width: 1100px; top: 150px; text-align: center; color: var(--white); font-size: 34px; font-weight: 500; line-height: 40px; }
  .brand-tagline { position: absolute; left: 0; width: 1100px; top: 200px; text-align: center; color: var(--white); font-size: 15px; font-weight: 700; line-height: 18px; text-transform: uppercase; }

  .steps-heading { position: absolute; left: 0; width: 1100px; top: 272px; text-align: center; font-size: 18px; font-weight: 700; line-height: 20px; color: var(--ink); text-transform: uppercase; }
  .steps-heading .highlight { color: var(--link-blue); }

  .step { position: absolute; top: 322px; width: 220px; height: 130px; text-align: center; font-weight: 700; text-transform: uppercase; }
  .step--call { left: 170px; background: var(--accent-yellow); color: var(--ink); }
  .step--details { left: 440px; background: var(--step-light); color: var(--ink); }
  .step--vehicle { left: 710px; background: var(--step-dark); color: var(--white); }
  .step-number { display: block; margin-top: 12px; font-size: 19px; font-weight: 500; }
  .step-icon { display: block; margin: 8px auto 5px; }
  .step-text { font-size: 11.5px; line-height: 13px; }
  .step-phone { font-size: 15px; line-height: 19px; }
  .step-arrow { position: absolute; top: 373px; }

  .referral-note { position: absolute; left: 0; width: 1100px; top: 462px; text-align: center; font-size: 15px; font-weight: 700; line-height: 20px; color: var(--link-blue); }

  .about-band { position: absolute; left: 0; top: 495px; width: 1100px; height: 240px; background: linear-gradient(180deg, var(--band-top) 0%, var(--band-bottom) 100%); }
  .about-title { position: absolute; left: 42px; width: 580px; top: 14px; text-align: center; color: var(--accent-yellow); font-size: 20px; font-weight: 700; line-height: 24px; }
  .about-copy { position: absolute; left: 42px; width: 580px; top: 42px; color: var(--white); font-family: "Roboto Condensed", sans-serif; font-weight: 300; font-size: 14.5px; line-height: 17.5px; text-align: justify; }

  .benefits-box { position: absolute; left: 680px; top: 18px; width: 378px; height: 204px; border: 9px solid var(--box-border); background: var(--box-fill); padding-top: 14px; }
  .benefits-title { text-align: center; color: var(--accent-yellow); font-size: 21px; font-weight: 700; line-height: 22px; text-transform: uppercase; }
  .benefits-list { list-style: none; margin: 14px 0 0 24px; display: grid; grid-template-columns: 172px 160px; row-gap: 10px; }
  .benefits-list li { position: relative; padding-left: 27px; color: var(--white); font-family: "Roboto Condensed", sans-serif; font-weight: 700; font-size: 19px; line-height: 21px; }
  .benefits-list svg { position: absolute; left: 0; top: 1px; }

  .flyer-footer { position: absolute; left: 0; top: 735px; width: 1100px; height: 45px; display: flex; align-items: center; justify-content: space-between; padding: 0 42px; color: var(--ink); font-size: 18px; font-weight: 500; }
  .social { display: flex; align-items: center; gap: 7px; }
  .social-dot { width: 21px; height: 21px; border-radius: 50%; background: #1a1a1a; }
</style>
</head>
<body>
  <main class="flyer">
    <div class="hero-photo hero-photo--car" role="img" aria-label="Photo of the front of a silver car parked on a street"></div>
    <div class="hero-photo hero-photo--drivers" role="img" aria-label="Photo of a smiling couple seated in a car"></div>

    <svg class="brand-banner" viewBox="0 0 1100 140" aria-hidden="true">
      <polygon points="290,0 810,0 775,140 325,140" fill="var(--brand-blue)"/>
    </svg>
    <div class="owned-badge" aria-hidden="true"></div>
    <h1 class="brand-name">Clear Road Rentals</h1>
    <p class="brand-tagline">Australia's No.1 Car Accident<br>Replacement Service</p>

    <h2 class="steps-heading">Arranging an acident replacement vehicle<br><span class="highlight">for yourself</span> is easy as <span class="highlight">1,2,3</span></h2>

    <div class="step step--call">
      <span class="step-number">1</span>
      <svg class="step-icon" width="20" height="20" viewBox="0 0 24 24" fill="none" stroke="#ffffff" stroke-width="1.6"><path d="M5 3h4l2 5-2.5 1.5a11 11 0 0 0 6 6L16 13l5 2v4a2 2 0 0 1-2 2A16 16 0 0 1 3 5a2 2 0 0 1 2-2z"/></svg>
      <p class="step-text">Call us on<br><span class="step-phone">1800 452 817</span><br>(Free call)</p>
    </div>
    <svg class="step-arrow" style="left:406px" width="18" height="28" viewBox="0 0 18 28"><path d="M4 4l10 10-10 10" fill="none" stroke="var(--link-blue)" stroke-width="2.2"/></svg>

    <div class="step step--details">
      <span class="step-number">2</span>
      <svg class="step-icon" width="28" height="24" viewBox="0 0 30 26" fill="none" stroke="#ffffff" stroke-width="1.6"><path d="M4 8h3l1.5 3.5-2 1a8 8 0 0 0 4 4l1-2 3.5 1.5v3a1.5 1.5 0 0 1-1.5 1.5A12 12 0 0 1 2.5 9.5 1.5 1.5 0 0 1 4 8z"/><ellipse cx="21" cy="7" rx="7" ry="5"/><path d="M17 11l-2 4 5-3"/></svg>
      <p class="step-text">Provide accident details</p>
    </div>
    <svg class="step-arrow" style="left:676px" width="18" height="28" viewBox="0 0 18 28"><path d="M4 4l10 10-10 10" fill="none" stroke="var(--link-blue)" stroke-width="2.2"/></svg>

    <div class="step step--vehicle">
      <span class="step-number">3</span>
      <svg class="step-icon" width="30" height="19" viewBox="0 0 32 20" fill="none" stroke="#ffffff" stroke-width="1.6"><path d="M3 14V10l4-1 4-5h10l5 5 3 1v4z"/><circle cx="9" cy="15" r="2.5"/><circle cx="23" cy="15" r="2.5"/></svg>
      <p class="step-text">You get a replacement<br>vehicle<br>We take care of the rest</p>
    </div>

    <p class="referral-note">When you call, please let us know where you got this flyer.</p>

    <section class="about-band">
      <h3 class="about-title">ABOUT US</h3>
      <p class="about-copy">Throughout Australia, there are a lot of people on the roads, especially in the main cities like Sydney and Melbourne. It's not uncommon to get into a car accident. Whether it's a simple fender bender or something more severe, your car could end up in a repair shop for repairs. The biggest problem that you now have to deal with is that while your vehicle is in the repair shop, you have no car. If the accident wasn't your fault, an accident replacement vehicle is available to you. You can call and schedule this replacement car so that you are not left without a car while it is under repairs. You shouldn't be inconvenienced just because someone else caused an accident. Knowing how to get a rental car and what the benefits will help you immensely.</p>

      <div class="benefits-box">
        <h3 class="benefits-title">We get your back<br>on the road today</h3>
        <ul class="benefits-list">
          <li><svg width="20" height="20" viewBox="0 0 22 22" fill="none" stroke="var(--accent-yellow)" stroke-width="2"><path d="M19 9.5A8.5 8.5 0 1 1 14 3"/><path d="M6.5 10l4 4 9-10"/></svg>Free Advice</li>
          <li><svg width="20" height="20" viewBox="0 0 22 22" fill="none" stroke="var(--accent-yellow)" stroke-width="2"><path d="M19 9.5A8.5 8.5 0 1 1 14 3"/><path d="M6.5 10l4 4 9-10"/></svg>Excess Waiver<br>Included</li>
          <li><svg width="20" height="20" viewBox="0 0 22 22" fill="none" stroke="var(--accent-yellow)" stroke-width="2"><path d="M19 9.5A8.5 8.5 0 1 1 14 3"/><path d="M6.5 10l4 4 9-10"/></svg>Free Delivery</li>
          <li><svg width="20" height="20" viewBox="0 0 22 22" fill="none" stroke="var(--accent-yellow)" stroke-width="2"><path d="M19 9.5A8.5 8.5 0 1 1 14 3"/><path d="M6.5 10l4 4 9-10"/></svg>Late Models<br>New vehicles</li>
        </ul>
      </div>
    </section>

    <footer class="flyer-footer">
      <span class="footer-web">www.clearroadrentals.com.au</span>
      <span class="social">Follow us on :&nbsp;<span class="social-dot" aria-hidden="true"></span><span class="social-dot" aria-hidden="true"></span></span>
    </footer>
  </main>
</body>
</html>
```